Bramble Roofing Website Relaunch

We require a re-launch of our website, We are a longrun roofing company based in New Zealand, we are rapidly expanding and require a more professionally presented website our current website is www.brambleroofing.co.nz we want something modern, masculine and communicates a "strong" "superior" image, we already have a logo which I have attached we use the orange and silver one as you will see on our current website

Industry/Entity Type

It Company

Number of Pages Required

1 page

Colors
f37122
f78f20
000000
1b1b1b
474747
d3d3d3
f5f5f5

Requirements
Must have
• Images of our work
• Email and Mobile Contact Details
• Link to social page circle page
• Who We Are, What We Do
• Certified Trade Craftsman Logo
• Our Logo

```html
<!DOCTYPE html>
<html lang="en">
<head>
<meta charset="utf-8">
<title>Bramble Roofing</title>
<link href="https://fonts.googleapis.com/css2?family=Cinzel:wght@400;700&family=Open+Sans:wght@400;600;700&family=Archivo+Black&display=swap" rel="stylesheet">
<style>
:root{
  --orange:#f37122;
  --orange-light:#f78f20;
  --black:#000000;
  --ink:#1b1b1b;
  --charcoal:#3a3a3a;
  --grey:#474747;
  --silver:#d3d3d3;
  --paper:#f5f5f5;
  --white:#ffffff;
  --body-grey:#8a8a8a;
}
*{margin:0;padding:0;box-sizing:border-box}
html,body{width:1200px;height:3120px;overflow:hidden;background:var(--white)}
body{position:relative;font-family:"Open Sans",Arial,sans-serif;color:var(--ink)}
.site-header{position:absolute;left:0;top:0;width:1200px;height:158px;background:var(--black)}
.brand{position:absolute;left:26px;top:38px;display:flex;align-items:center;gap:16px}
.brand-mark{width:70px;height:70px;border:4px solid var(--silver);transform:rotate(45deg)}
.brand-name{font-family:"Cinzel",serif;font-weight:700;font-size:40px;color:var(--orange);letter-spacing:1px;line-height:1}
.contact-bar{position:absolute;right:40px;top:22px;display:flex;gap:34px;align-items:center}
.contact-item{display:flex;align-items:center;gap:12px;color:var(--white);font-weight:700;font-size:19px}
.contact-item.phone{font-size:24px;letter-spacing:1px}
.icon-diamond{width:46px;height:46px;display:block}
.main-nav{position:absolute;right:36px;top:92px;display:flex;align-items:center;gap:34px}
.main-nav a{color:var(--white);text-decoration:none;font-weight:700;font-size:18px;text-transform:uppercase}
.main-nav a.active{display:flex;align-items:center;justify-content:center;width:72px;height:56px;position:relative;color:var(--orange)}
.main-nav a.active::before{content:"";position:absolute;inset:6px 14px;border:3px solid var(--orange);transform:rotate(45deg)}
.hero{position:absolute;left:0;top:158px;width:1200px;height:605px;overflow:hidden}
.hero-photo{position:absolute;inset:0;background:linear-gradient(180deg,#b9c3cc 0%,#d9dde0 25%,#5f6a48 45%,#6b6f6e 60%,#494c4e 100%)}
.hero-title{position:absolute;left:0;right:0;top:40px;text-align:center;font-family:"Open Sans",sans-serif;font-weight:700;font-size:54px;line-height:58px;color:var(--orange);text-transform:uppercase}
.hero-arrow{position:absolute;top:218px;width:82px;height:82px}
.hero-arrow.prev{left:10px}.hero-arrow.next{right:10px}
.hero-dots{position:absolute;left:552px;top:572px;display:flex;gap:10px}
.hero-dots span{width:18px;height:18px;border-radius:50%;border:3px solid var(--orange)}
.hero-dots span.on{background:var(--orange)}
.cert-badge{position:absolute;right:12px;top:406px;width:195px;height:195px;background:var(--white);border-radius:6px;display:flex;align-items:center;justify-content:center}
.cert-badge i{width:150px;height:150px;border-radius:50%;border:10px solid var(--ink);display:block}
.section-heading{text-align:center;font-family:"Open Sans",sans-serif;font-weight:600;font-size:40px;line-height:46px;text-transform:uppercase}
.section-heading::after{content:"";display:block;width:86px;height:10px;background:var(--orange);margin:10px auto 0}
.section-copy{font-family:"Cinzel",serif;font-size:13.5px;line-height:34px;color:var(--body-grey);text-align:center;text-transform:uppercase}
.who{position:absolute;left:0;top:763px;width:1200px;height:331px;padding:30px 44px 0}
.who .section-copy{margin-top:30px}
.team{position:absolute;left:0;top:1094px;width:1200px;height:653px;background:var(--charcoal);padding-top:14px}
.team .section-heading{color:var(--white)}
.member{position:absolute;left:50px;width:1110px;display:flex;gap:24px}
.member-photo{flex:none;width:128px;height:128px;border-radius:50%;border:5px solid var(--silver);background:radial-gradient(circle,#8a8a7c,#5a6552)}
.member-name{font-family:"Open Sans",sans-serif;font-weight:700;font-size:31px;color:var(--white);text-transform:uppercase;line-height:40px;margin-top:8px}
.member-bio{font-family:"Cinzel",serif;font-size:13px;line-height:34px;color:var(--silver);text-transform:uppercase}
.what{position:absolute;left:0;top:1747px;width:1200px;height:245px;padding:12px 60px 0;border-bottom:2px solid var(--silver)}
.what .section-copy{margin-top:18px}
.work{position:absolute;left:0;top:1992px;width:1200px;height:739px;padding:18px 60px 0}
.work .section-copy{margin-top:8px}
.work-photo{position:absolute;left:43px;top:221px;width:1102px;height:489px;background:linear-gradient(180deg,#9aa0a6 0%,#c9ccce 20%,#4a4e52 38%,#5c5f62 62%,#b8b6ad 78%,#5e6e3e 100%)}
.work-dots{position:absolute;left:474px;top:668px;display:flex;gap:6px}
.work-dots span{width:17px;height:17px;border-radius:50%;border:3px solid var(--orange)}
.work-dots span.on{background:var(--orange)}
.site-footer{position:absolute;left:0;top:2731px;width:1200px;height:341px;background:var(--charcoal);color:var(--white)}
.footer-col{position:absolute;top:0;height:341px}
.footer-brand{left:40px;width:300px;text-align:center;padding-top:26px}
.footer-brand .brand-name{font-size:34px;color:var(--silver)}
.footer-brand .row{display:flex;align-items:center;justify-content:center;gap:12px}
.footer-brand .brand-mark{width:50px;height:50px;border-width:3px}
.footer-tag{font-family:"Archivo Black",sans-serif;font-size:13px;line-height:22px;margin-top:14px}
.follow{font-family:"Archivo Black",sans-serif;font-size:22px;margin-top:18px}
.social-dot{width:54px;height:54px;border-radius:50%;background:#3b5fb0;margin:10px auto 0}
.divider{position:absolute;top:30px;width:2px;height:286px;background:var(--silver)}
.footer-contact{left:494px;width:380px;padding-top:40px}
.footer-contact h3{font-family:"Archivo Black",sans-serif;font-size:26px;font-weight:400;text-decoration:underline}
.footer-contact p{font-family:"Archivo Black",sans-serif;font-size:17px;text-decoration:underline;margin-top:26px;color:var(--silver)}
.footer-mail{left:906px;width:280px;padding-top:40px;text-align:center}
.footer-mail h3{font-family:"Archivo Black",sans-serif;font-size:26px;font-weight:400}
.field{display:block;width:276px;height:38px;margin:26px auto 0;border:2px solid var(--silver);background:var(--charcoal);color:var(--white);font:700 15px "Open Sans",sans-serif;text-align:left;padding:8px 10px}
.field+.field{margin-top:14px}
.field.msg{height:72px}
.submit{display:block;width:126px;height:34px;margin:14px 0 0 76px;border:2px solid var(--silver);color:var(--white);font:700 15px "Open Sans",sans-serif;line-height:30px}
.copyright{position:absolute;left:0;top:3072px;width:1200px;height:48px;background:var(--ink);color:var(--white);text-align:center;font-family:"Archivo Black",sans-serif;font-size:15px;line-height:48px;border-top:2px solid var(--grey)}
</style>
</head>
<body>
<header class="site-header">
  <div class="brand"><span class="brand-mark"></span><span class="brand-name">Bramble Roofing</span></div>
  <div class="contact-bar">
    <div class="contact-item">
      <svg class="icon-diamond" viewBox="0 0 46 46"><rect x="9" y="9" width="28" height="28" transform="rotate(45 23 23)" fill="none" stroke="#fff" stroke-width="3"/><rect x="15" y="17" width="16" height="12" fill="none" stroke="#fff" stroke-width="2"/><path d="M15 17l8 7 8-7" fill="none" stroke="#fff" stroke-width="2"/></svg>
      HELLO@BRAMBLEROOFING.CO.NZ
    </div>
    <div class="contact-item phone">
      <svg class="icon-diamond" viewBox="0 0 46 46"><rect x="9" y="9" width="28" height="28" transform="rotate(45 23 23)" fill="none" stroke="#fff" stroke-width="3"/><path d="M17 15c-2 2-1 7 4 12s10 6 12 4l-3-4-3 2c-2-1-5-4-6-6l2-3z" fill="#fff"/></svg>
      021 555 01420
    </div>
  </div>
  <nav class="main-nav">
    <a class="active" href="#home"><span style="position:relative">HOME</span></a>
    <a href="#about">About</a><a href="#services">Services</a><a href="#work">Our Work</a><a href="#contact">Contact</a>
  </nav>
</header>

<section class="hero">
  <div class="hero-photo" role="img" aria-label="Photo of a completed longrun roof on a modern single-storey home"></div>
  <h1 class="hero-title">The Specilists<br>Rofing</h1>
  <svg class="hero-arrow prev" viewBox="0 0 82 82"><circle cx="41" cy="41" r="41" fill="#000"/><path d="M48 22L28 41l20 19" fill="none" stroke="#f37122" stroke-width="4"/></svg>
  <svg class="hero-arrow next" viewBox="0 0 82 82"><circle cx="41" cy="41" r="41" fill="#000"/><path d="M34 22l20 19-20 19" fill="none" stroke="#f37122" stroke-width="4"/></svg>
  <div class="hero-dots"><span></span><span class="on"></span><span></span></div>
  <div class="cert-badge" role="img" aria-label="Certified Trade Craftsman badge"><i></i></div>
</section>

<section class="who" id="about">
  <h2 class="section-heading">Who We Are:</h2>
  <p class="section-copy">We are a local, family owned and operated company with over 18 years extensive experience in the roofing industry, roofing not only Waikato and Auckland but surrounding areas also. We are committed to providing superior service to our customers regardless of how big or small your project is, your satisfaction is our guarantee. We take pride in installing quality products, offering a workmanship guarantee and manufacturers material warranties where applicable. In a fast paced advancing industry we are constantly striving to provide the latest, modern quality installation methods available to ensure customer expectations are exceeded, project targets are met and a high quality finished product is delivered every time</p>
</section>

<section class="team">
  <h2 class="section-heading">Our Team:</h2>
  <div class="member" style="top:86px">
    <div class="member-photo" role="img" aria-label="Portrait photo of Rowan"></div>
    <div><h3 class="member-name">Rowan "The Boss"</h3>
    <p class="member-bio">Rowan started Bramble Roofing fulfilling his dream of owning his own business after 18+ years in the roofing industry. His focus, integrity and unrivalled level of expertise ensures he remains a leader in the industry, increasingly in demand and a reputable installer of choice.</p></div>
  </div>
  <div class="member" style="top:270px">
    <div class="member-photo" role="img" aria-label="Portrait photo of Kieran Holt"></div>
    <div><h3 class="member-name">Kieran Holt</h3>
    <p class="member-bio">Kieran has been in the industry for 10+ years, having entered into roofing straight from school. He has expertise in all roofing installations as well as experience in roofing installations in Australia. Kieran is proficient in complex, creative finishing and flashing systems</p></div>
  </div>
  <div class="member" style="top:442px">
    <div class="member-photo" role="img" aria-label="Portrait photo of Marina Felde"></div>
    <div><h3 class="member-name">Marina Felde</h3>
    <p class="member-bio">Marina is Rowan's wife and office manager, she works full time off site, with an employment history of 15+ years in the construction, materials handling equipment and project administration sectors. Her spare time is taken up managing Bramble Roofing, facilitating the daily operations, many clerical positions, health and safety and ensuring client enquires are responded too timely.</p></div>
  </div>
</section>

<section class="what" id="services">
  <h2 class="section-heading">What We Do:</h2>
  <p class="section-copy">At Bramble Roofing we offer a variety of professional services specializing in residential, industrial and commercial long run roofing installations &#9830; new roofs and re-roofs &#9830; metal cladding &#9830; spouting and metal fascia &#9830; down pipes &#9830; alterations &#9830;<br>We offer a no obligation free quotation, inspection and consultation service.<br>Providing un-biased, honest advice whilst determining services required.</p>
</section>

<section class="work" id="work">
  <h2 class="section-heading">Our Work:</h2>
  <p class="section-copy">At Bramble Roofing we offer a variety of professional services specializing in residential, industrial and commercial long run roofing installations &#9830; new roofs and re-roofs &#9830; metal cladding &#9830; spouting and metal fascia &#9830; down pipes &#9830; alterations &#9830;<br>We offer a no obligation free quotation, inspection and consultation service.<br>Providing un-biased, honest advice whilst determining services required.</p>
  <div class="work-photo" role="img" aria-label="Photo of a new dark metal roof on a house under construction with scaffolding"></div>
  <div class="work-dots"><span></span><span></span><span></span><span></span><span></span><span class="on"></span><span></span><span></span><span></span><span></span></div>
</section>

<footer class="site-footer" id="contact">
  <div class="footer-col footer-brand">
    <div class="row"><span class="brand-mark"></span><span class="brand-name">Bramble Roofing</span></div>
    <p class="footer-tag">LOREM IPSUM DOLOR SIT AMET,<br>CONSECTETUR ADIPISCING ELIT, SED<br>DO EIUSMOD TEMPOR INCIDIDUNT UT</p>
    <p class="follow">FOLLOW US ON:</p>
    <div class="social-dot" role="img" aria-label="Social page link"></div>
  </div>
  <span class="divider" style="left:376px"></span>
  <div class="footer-col footer-contact">
    <h3>CONTACT US:</h3>
    <p>PHONE:021 555 01420</p>
    <p>EMAIL:HELLO@BRAMBLEROOFING.CO.NZ</p>
    <p>ADDRESS:438 YOUR STREET</p>
  </div>
  <span class="divider" style="left:868px"></span>
  <div class="footer-col footer-mail">
    <h3>SEND MAIL:</h3>
    <span class="field">NAME..</span>
    <span class="field">EMAIL..</span>
    <span class="field msg">MSG..</span>
    <span class="submit">SUBMITE</span>
  </div>
</footer>
<div class="copyright">COPYRIGHT ALL RIGHT RESERVED</div>
</body>
</html>
```